BARRIER BANNER OTP

I am looking for a visual for a banner
3 meters long by 1 high.
In the same theme as the visual identity of the company.
As simple as possible without overloading

There must be the LOGO, the title TECHNIQUE SERVICES ROUSSEL

_________________________

I am looking for a visual for a banner (barrier banner)
3 meters long by 1 high.

AIR CONDITIONING HEATING VENTILATION
04 52 31 64 19

Font styles to use
Sans Serif

Colors
33b8a4
00a990
33a6d7
0493ce
3176b5
0355a3
ffffff

Requirements
Should not have
• No photo
No photo

```html
<!DOCTYPE html>
<html lang="en">
<head>
<meta charset="utf-8">
<title>OTP – Barrier Banner</title>
<link rel="stylesheet" href="https://fonts.googleapis.com/css2?family=Archivo:wght@700;800;900&display=swap">
<style>
  :root {
    --ink: #2b3945;
    --headline: #0b7ea7;
    --band: #0e3b5e;
    --sky-light: #e6f5fb;
    --sky: #a3dbee;
    --teal: #00a990;
    --white: #ffffff;
    --page: #ffffff;
  }
  * { margin: 0; padding: 0; box-sizing: border-box; }
  html, body {
    width: 1200px;
    height: 800px;
    overflow: hidden;
    background: var(--page);
    font-family: "Archivo", Arial, sans-serif;
  }
  .banner {
    position: absolute;
    left: 30px;
    top: 210px;
    width: 1140px;
    height: 380px;
    border-radius: 26px 26px 6px 6px;
    overflow: hidden;
    background: linear-gradient(90deg, var(--white) 0%, var(--white) 36%, var(--sky-light) 50%, var(--sky) 68%, var(--sky) 100%);
  }
  .brand {
    position: absolute;
    left: 30px;
    top: 28px;
    display: flex;
    align-items: center;
    gap: 14px;
  }
  .brand-mark {
    width: 26px;
    height: 26px;
    background: var(--teal);
  }
  .brand-name {
    font-weight: 900;
    font-size: 112px;
    line-height: 1;
    letter-spacing: 2px;
    color: var(--ink);
  }
  .company-name {
    position: absolute;
    left: 380px;
    top: 36px;
    font-weight: 900;
    font-size: 34px;
    line-height: 1.45;
    color: var(--ink);
    letter-spacing: 0.5px;
  }
  .services {
    position: absolute;
    left: 30px;
    top: 205px;
    font-weight: 900;
    font-size: 43px;
    line-height: 1.08;
    color: var(--headline);
    letter-spacing: 0.5px;
  }
  .scene {
    position: absolute;
    left: 640px;
    top: 20px;
    width: 490px;
    height: 308px;
    border-radius: 6px;
    background: linear-gradient(180deg, #b9e4f2 0%, #9fd6ea 70%, #7fb9d3 100%);
  }
  .contact-band {
    position: absolute;
    left: 0;
    bottom: 0;
    width: 100%;
    height: 52px;
    background: var(--band);
    display: flex;
    align-items: center;
    padding-left: 30px;
    color: var(--white);
  }
  .phone {
    font-weight: 800;
    font-size: 32px;
    letter-spacing: 1px;
  }
  .divider {
    width: 3px;
    height: 38px;
    background: var(--white);
    margin: 0 20px;
  }
  .website {
    font-weight: 700;
    font-size: 17px;
  }
</style>
</head>
<body>
  <main class="banner">
    <div class="brand">
      <span class="brand-name">OTP</span>
      <span class="brand-mark"></span>
    </div>

    <h1 class="company-name">TECHNIQUE<br>SERVICES<br>ROUSSEL</h1>

    <h2 class="services">AIR CONDITIONING<br>HEATING VENTILATION</h2>

    <div class="scene" role="img" aria-label="Illustration of two technicians installing an indoor air conditioning unit and an outdoor condenser, with a plant, toolbox and city-view window"></div>

    <footer class="contact-band">
      <span class="phone">04 52 31 64 19</span>
      <span class="divider"></span>
      <span class="website">technique-services-roussel.fr</span>
    </footer>
  </main>
</body>
</html>
```